Brimvantel

We are re-branding the company with a new logo (attached) which I would
like to go on one side of the card, and I have attached a file showing what
the old back side looked like, and I do like the characters that show the
phone, e-mails, etc., I don't like the current arrangement, and I want
something clean, clear and out of the box, as we are an aviation consulting
firm, and we work outside of the box.

```html
<!DOCTYPE html>
<html lang="en">
<head>
<meta charset="utf-8">
<title>Brimvantel – Business Card</title>
<link href="https://fonts.googleapis.com/css2?family=Open+Sans:wght@400;600;700&display=swap" rel="stylesheet">
<style>
  :root {
    --backdrop: #d9d6d2;
    --card: #1c1c1d;
    --card-edge: #262627;
    --red: #d42a2e;
    --grey: #8d8d8f;
    --light: #e4e4e4;
    --muted: #bdbdbd;
    --rule: #4a4a4c;
    --faint: #2a2a2b;
  }
  * { box-sizing: border-box; margin: 0; padding: 0; }
  html, body { width: 1200px; height: 817px; overflow: hidden; }
  body {
    background: var(--backdrop);
    font-family: "Open Sans", Arial, sans-serif;
    position: relative;
  }
  .card {
    position: absolute;
    top: 254px;
    width: 540px;
    height: 309px;
    background: linear-gradient(160deg, var(--card-edge), var(--card) 60%);
    border-radius: 6px;
    overflow: hidden;
  }
  .card--back { left: 40px; }
  .card--front { left: 620px; }

  /* back side */
  .mark-faint {
    position: absolute;
    left: 40px; top: 40px;
    width: 230px; height: 230px;
    border-radius: 50%;
    background: var(--faint);
  }
  .services {
    position: absolute;
    left: 60px; top: 30px;
    list-style: none;
  }
  .services li {
    color: var(--light);
    font-size: 15px;
    line-height: 25px;
    display: flex;
    align-items: center;
    gap: 9px;
  }
  .services li::before {
    content: "";
    width: 9px; height: 9px;
    border-radius: 50%;
    background: var(--light);
  }
  .brand {
    position: absolute;
    display: flex;
    flex-direction: column;
  }
  .brand__name {
    color: var(--red);
    font-weight: 700;
    letter-spacing: 1px;
  }
  .brand__tagline {
    color: var(--grey);
  }
  .card--back .brand { left: 230px; top: 220px; }
  .card--back .brand__name { font-size: 30px; line-height: 32px; }
  .card--back .brand__tagline { font-size: 13px; }

  /* front side */
  .card--front .brand {
    right: 40px; top: 46px;
    align-items: flex-end;
  }
  .brand__row { display: flex; align-items: center; gap: 14px; }
  .brand__dot {
    width: 46px; height: 46px; border-radius: 50%;
    background: var(--light);
  }
  .card--front .brand__name { font-size: 40px; line-height: 44px; }
  .card--front .brand__tagline { font-size: 16px; margin-top: 2px; }

  .person {
    position: absolute;
    left: 28px; top: 160px;
    width: 218px;
    text-align: right;
  }
  .person__name {
    color: var(--red);
    font-weight: 700;
    font-size: 21px;
    line-height: 26px;
  }
  .person__role, .person__address {
    color: var(--muted);
    font-size: 14px;
    line-height: 20px;
  }
  .person__role { margin-bottom: 2px; }
  .divider {
    position: absolute;
    left: 262px; top: 170px;
    width: 1px; height: 112px;
    background: var(--rule);
  }
  .contacts {
    position: absolute;
    left: 278px; top: 168px;
    list-style: none;
  }
  .contacts li {
    display: flex;
    align-items: center;
    gap: 8px;
    color: var(--light);
    font-size: 14px;
    line-height: 23px;
  }
  .contacts svg { width: 12px; height: 12px; fill: var(--red); flex: none; }
</style>
</head>
<body>

  <section class="card card--back" aria-label="Card back">
    <div class="mark-faint" aria-hidden="true"></div>
    <ul class="services">
      <li>Airline Certification</li>
      <li>Aircraft finance/leasing</li>
      <li>Technical services</li>
      <li>Aviation consulting</li>
      <li>Airline Restructuring</li>
    </ul>
    <div class="brand">
      <span class="brand__name">BRIMVANTEL</span>
      <span class="brand__tagline">seasoned insight . reliable results</span>
    </div>
  </section>

  <section class="card card--front" aria-label="Card front">
    <div class="brand">
      <div class="brand__row">
        <span class="brand__name">BRIMVANTEL</span>
        <span class="brand__dot" aria-hidden="true"></span>
      </div>
      <span class="brand__tagline">seasoned insight . reliable results</span>
    </div>

    <div class="person">
      <p class="person__name">Daniel R. Hollace</p>
      <p class="person__role">Managing Member</p>
      <p class="person__address">2210 Harbor Field Lane,<br>Westbrook, CA 95714</p>
    </div>

    <div class="divider"></div>

    <ul class="contacts">
      <li>
        <svg viewBox="0 0 12 12" aria-hidden="true"><path d="M2.5 0.5l2 2.2-1 1.3c.8 1.7 2.1 3 3.8 3.8l1.3-1 2.2 2-1.2 2.2C4.8 10.6 1.4 7.2.4 1.7z"/></svg>
        (555) 214-3380
      </li>
      <li>
        <svg viewBox="0 0 12 12" aria-hidden="true"><rect x="3" y="0.5" width="6" height="3"/><rect x="0.5" y="4" width="11" height="5" rx="1"/><rect x="3" y="8" width="6" height="3.5"/></svg>
        (555) 214-3381
      </li>
      <li>
        <svg viewBox="0 0 12 12" aria-hidden="true"><path d="M3.5 0.5h5a1 1 0 0 1 1 1v9a1 1 0 0 1-1 1h-5a1 1 0 0 1-1-1v-9a1 1 0 0 1 1-1zM4 2v7h4V2z"/></svg>
        (555) 907-4412
      </li>
      <li>
        <svg viewBox="0 0 12 12" aria-hidden="true"><path d="M0.5 2.5h11v7h-11z M0.5 2.5L6 7l5.5-4.5" fill="none" stroke="#d42a2e" stroke-width="1.2"/></svg>
        daniel@brimvantel-air.com
      </li>
      <li>
        <svg viewBox="0 0 12 12" aria-hidden="true"><g fill="none" stroke="#d42a2e" stroke-width="1.1"><circle cx="6" cy="6" r="5.2"/><ellipse cx="6" cy="6" rx="2.2" ry="5.2"/><path d="M0.8 6h10.4"/></g></svg>
        www.brimvantel-air.com
      </li>
    </ul>
  </section>

</body>
</html>
```